Wine label for premium wine of vinery Bralovnik.

Design Premium wine label.

The brand is called Tellovra. Brand can be extended to Marzeno Tellovra. There
The label should be unique and high class feeling.
This is facebook lonk of the winery
https://www.plaverio.example/408113925076431/

On facebook you can see some examole of labels that are used now. Winery is called Bralovnik, so they used letter "B" as a logo in different ways

Target Market(s)

Premium high class yet modern living traditional but also gadget fun.
I have uploaded few inspirational photos that the owner of the vinery likes. Hope it helps.

Industry/Entity Type

Vinery

Requirements
Must have
• Black, gold, silver color to be dominated. Colors that are NOT acceptable are: green, yellow, blue, purple, pink.

The name of the vinary is Bralovnik and it should be on the front label.
Nice to have
• The size of label should fit the Grapsy application screenshot frame.
Should not have
• Cheap perception of the label and brand

```html
<!DOCTYPE html>
<html lang="en">
<head>
<meta charset="utf-8">
<title>Tellovra Cabernet Sauvignon 2018 – Label</title>
<link href="https://fonts.googleapis.com/css2?family=Montserrat:wght@400;500&family=Raleway:wght@500&display=swap" rel="stylesheet">
<style>
  :root {
    --backdrop: #5f6062;
    --label-black: #1e1d1c;
    --label-edge: #151414;
    --gold: #c9a774;
    --gold-deep: #9c6a45;
    --gold-light: #e6cf96;
    --silver: #d8d8d8;
  }
  html, body {
    margin: 0;
    padding: 0;
    width: 1200px;
    height: 1200px;
    overflow: hidden;
    background: var(--backdrop);
  }
  .label {
    position: absolute;
    left: 303px;
    top: 112px;
    width: 594px;
    height: 1030px;
    background: linear-gradient(90deg, var(--label-edge) 0%, var(--label-black) 30%, #262524 55%, var(--label-black) 80%, var(--label-edge) 100%);
    overflow: hidden;
  }
  .brand-name {
    position: absolute;
    left: 0;
    right: 0;
    top: 138px;
    margin: 0;
    text-align: center;
    font-family: "Raleway", sans-serif;
    font-weight: 500;
    font-size: 54px;
    letter-spacing: 14px;
    padding-left: 14px;
    color: var(--gold);
    line-height: 1;
  }
  .wine-details {
    position: absolute;
    right: 37px;
    top: 370px;
    text-align: right;
    color: var(--silver);
    font-family: "Montserrat", sans-serif;
  }
  .variety {
    margin: 0;
    font-weight: 500;
    font-size: 22px;
    letter-spacing: 1.5px;
    line-height: 38px;
  }
  .vintage {
    margin: 20px 0 0;
    font-weight: 400;
    font-size: 15px;
    letter-spacing: 6px;
    margin-right: -6px;
  }
  .winery {
    margin: 52px 0 0;
    font-weight: 500;
    font-size: 12px;
    letter-spacing: 0.6px;
  }
  .wave-field {
    position: absolute;
    left: 0;
    bottom: 0;
    width: 594px;
    height: 440px;
    display: block;
  }
</style>
</head>
<body>
  <main class="label">
    <h1 class="brand-name">TELLOVRA</h1>

    <section class="wine-details">
      <p class="variety">CABERNET<br>SAUVIGNON</p>
      <p class="vintage">2018</p>
      <p class="winery">VINARIJA BRALOVNIK</p>
    </section>

    <svg class="wave-field" viewBox="0 0 594 440" role="img" aria-label="Flowing pattern of fine gold and copper wave lines rising across the lower label like rolling vineyard hills">
      <defs>
        <linearGradient id="wave-tone" x1="0" y1="0" x2="1" y2="1">
          <stop offset="0" stop-color="var(--gold-deep)" stop-opacity="0.55"/>
          <stop offset="0.5" stop-color="var(--gold)" stop-opacity="0.45"/>
          <stop offset="1" stop-color="var(--gold-light)" stop-opacity="0.35"/>
        </linearGradient>
      </defs>
      <path d="M0 112 C 70 125, 150 120, 260 96 C 380 68, 470 52, 594 46 L 594 440 L 0 440 Z" fill="url(#wave-tone)"/>
    </svg>
  </main>
</body>
</html>
```